Patient Engagement Solution

We need an attractive and easy-to-use GUI for patients and clinicians, which includes screens and icons. The application has been named Quorvix. I have our corporate logo attached as well.
I have attached the screens that the developer has used to create the solution, but we all know they miss the target when it comes to the creative stuff.
If it helps, I can supply some competitor's screens as a guide - please let me know.

Target Market(s)

Patients and Clinicians

Industry/Entity Type

Healthcare/Hospitals

Font styles to use
Other font styles liked:
• Easy to Read

Requirements
Must have
• Attractive, easy to use graphical user interface. Screen size is usually 22" 16:9
Nice to have
• Inviting and interesting look
Should not have
• Complicated hard to navigate screens

```html
<!DOCTYPE html>
<html lang="en">
<head>
<meta charset="utf-8">
<title>Quorvix – Patient Engagement Screens</title>
<link rel="stylesheet" href="https://fonts.googleapis.com/css2?family=Oswald:wght@400;500;600&display=swap">
<style>
  :root{
    --page-bg:#f2f2f2;
    --screen-bg:#fbfbfb;
    --header-bg:#121212;
    --accent:#e8222a;
    --tile-pink:#fde6e8;
    --label-bg:#2a2a2a;
    --search-bg:#5f5f5f;
    --search-btn:#8a8a8a;
    --ink:#2a2a2a;
    --deco-pink:rgba(240,150,160,.16);
  }
  *{box-sizing:border-box;margin:0;padding:0}
  html,body{width:1200px;height:2245px;overflow:hidden;background:var(--page-bg)}
  body{position:relative;font-family:"Oswald",sans-serif;color:var(--ink)}

  .screen{position:absolute;width:1064px;height:662px;background:var(--screen-bg);
    border-left:3px solid var(--accent);overflow:hidden;box-shadow:0 2px 6px rgba(0,0,0,.08)}
  .screen--home{left:57px;top:52px}
  .screen--services{left:68px;top:765px}
  .screen--languages{left:60px;top:1496px}

  .deco{position:absolute;background:var(--deco-pink);border-radius:26px}
  .deco--right{width:220px;height:420px;right:-90px;top:80px;transform:rotate(-22deg)}
  .deco--bottom{width:420px;height:300px;left:560px;top:560px;transform:rotate(-22deg)}

  .topbar{position:absolute;left:0;top:0;width:100%;height:64px;background:var(--header-bg)}
  .brand{position:absolute;left:28px;top:18px;display:flex;align-items:center;gap:8px;
    color:#fff;font-size:18px;font-weight:500;letter-spacing:.3px}
  .brand-dot{width:12px;height:12px;border-radius:50%;background:var(--accent)}
  .search{position:absolute;left:644px;top:12px;width:350px;height:40px;background:var(--search-bg);
    border-radius:4px;overflow:hidden}
  .search-text{position:absolute;left:21px;top:9px;color:#fff;font-size:14px;font-weight:400}
  .search-btn{position:absolute;right:0;top:0;width:48px;height:40px;background:var(--search-btn);
    display:flex;align-items:center;justify-content:center}

  .tile{position:absolute;width:148px;height:160px;background:var(--tile-pink);border-radius:4px;overflow:hidden}
  .tile-icon{position:absolute;left:0;top:0;width:100%;height:126px;display:flex;align-items:center;justify-content:center}
  .tile-icon svg{width:74px;height:74px;fill:none;stroke:var(--accent);stroke-width:2.4;stroke-linecap:round;stroke-linejoin:round}
  .tile-icon .flag{width:80px;height:52px;stroke:none}
  .tile-label{position:absolute;left:0;bottom:0;width:100%;height:34px;background:var(--label-bg);
    color:#fff;font-size:21px;font-weight:600;text-align:center;line-height:34px;letter-spacing:.2px;
    border-radius:3px 3px 4px 4px}
  .icon-placeholder{width:60px;height:60px;border-radius:50%;background:rgba(232,34,42,.18)}

  .ward-clock{position:absolute;width:140px;text-align:center;line-height:1;font-weight:600}
  .ward-clock .ward,.ward-clock .bed{font-size:22px;color:var(--ink);display:block}
  .ward-clock .time{font-size:46px;color:var(--accent);display:block;margin:-2px 0 -3px}
  .screen--home .ward-clock{left:845px;top:530px}
  .screen--services .ward-clock{left:843px;top:542px}
  .screen--languages .ward-clock{left:846px;top:529px}
</style>
</head>
<body>

<svg width="0" height="0" style="position:absolute" aria-hidden="true">
  <defs>
    <symbol id="i-rocket" viewBox="0 0 48 48"><path d="M40 8s-9-1-16 6l-8 10 8 8 10-8c7-7 6-16 6-16z"/><circle cx="31" cy="17" r="3.5"/><path d="M16 24l-6 1 4-6h6M24 32l-1 6 6-4v-6M12 34l-5 5M15 37l-4 4M10 31l-4 4"/></symbol>
    <symbol id="i-tv" viewBox="0 0 48 48"><rect x="6" y="14" width="36" height="24" rx="3"/><rect x="10" y="18" width="22" height="16" rx="1"/><path d="M17 7l7 7 7-7M37 20v2M37 26v6M12 38v3M36 38v3"/></symbol>
    <symbol id="i-radio" viewBox="0 0 48 48"><path d="M8 16l32-8"/><rect x="6" y="16" width="36" height="24" rx="3"/><path d="M6 24h36"/><circle cx="14" cy="32" r="3"/><circle cx="34" cy="32" r="3"/><path d="M19 32h10M32 19v3M36 19v3"/></symbol>
    <symbol id="i-apps-web" viewBox="0 0 48 48"><rect x="5" y="7" width="36" height="30" rx="2"/><path d="M5 13h36M9 10h2M13 10h2M20 10h16M9 18h12M9 23h12M9 28h12M9 33h10"/><rect x="25" y="18" width="14" height="24" rx="2"/><circle cx="32" cy="29" r="4"/><path d="M30 29l1.5 1.5L34 28M30 39h4"/></symbol>
    <symbol id="i-language" viewBox="0 0 48 48"><rect x="5" y="6" width="20" height="20" rx="2"/><rect x="23" y="22" width="20" height="20" rx="2"/><path d="M10 11h10M15 9v2M11 20c4-2 6-5 7-9M13 14c2 3 4 5 7 6M28 38l5-12 5 12M30 34h6M30 6c5 0 9 3 9 8l2-2M8 30c0 5 4 9 9 9l-2 2"/></symbol>
    <symbol id="i-clock" viewBox="0 0 48 48"><circle cx="24" cy="26" r="15"/><path d="M24 17v9l6 5M6 12a8 8 0 0 1 9-5M42 12a8 8 0 0 0-9-5M14 40l-3 4M34 40l3 4"/></symbol>
    <symbol id="i-video" viewBox="0 0 48 48"><rect x="4" y="13" width="28" height="22" rx="4"/><path d="M32 21l12-7v20l-12-7z"/></symbol>
    <symbol id="i-globe" viewBox="0 0 48 48"><circle cx="24" cy="24" r="18"/><ellipse cx="24" cy="24" rx="8" ry="18"/><path d="M6 24h36M9 14h30M9 34h30M24 6v36"/></symbol>
    <symbol id="i-clinical" viewBox="0 0 48 48"><circle cx="24" cy="11" r="6"/><path d="M24 8v6M21 11h6M6 18h12M30 18h12M9 18v24M39 18v24M5 42h38M17 28h14v14H17zM24 28v14M13 22h4M31 22h4"/></symbol>
    <symbol id="i-education" viewBox="0 0 48 48"><path d="M3 19l21-9 21 9-21 9z"/><path d="M12 23v9c0 4 24 4 24 0v-9M42 20v12"/><path d="M40 36l2-4 2 4-2 3z"/></symbol>
    <symbol id="i-meal" viewBox="0 0 48 48"><path d="M5 36h38M9 34a15 15 0 0 1 30 0z"/><circle cx="24" cy="16" r="2.5"/><path d="M15 28a9 9 0 0 1 6-7"/></symbol>
    <symbol id="i-books" viewBox="0 0 48 48"><path d="M6 16l26-6 10 3-26 6zM6 16v5l10 3 26-6v-5M6 24v5l10 3 26-6v-5M6 32v5l10 3 26-6v-5" fill="rgba(232,34,42,.9)"/></symbol>
    <symbol id="i-gear" viewBox="0 0 48 48"><circle cx="24" cy="24" r="6"/><path d="M21 5h6l1 5 4 2 4-3 4 4-3 4 2 4 5 1v6l-5 1-2 4 3 4-4 4-4-3-4 2-1 5h-6l-1-5-4-2-4 3-4-4 3-4-2-4-5-1v-6l5-1 2-4-3-4 4-4 4 3 4-2z"/></symbol>
    <symbol id="i-phone-apps" viewBox="0 0 48 48"><rect x="13" y="4" width="22" height="40" rx="3"/><path d="M13 10h22M13 37h22M22 41h4"/><rect x="17" y="14" width="6" height="6"/><rect x="25" y="14" width="6" height="6"/><rect x="17" y="24" width="6" height="6"/><rect x="25" y="24" width="6" height="6"/></symbol>
    <symbol id="i-phone" viewBox="0 0 48 48"><path d="M12 7l6 0 3 9-4 3c2 5 6 9 11 11l3-4 9 3v6c0 3-3 5-6 4C21 36 12 27 9 14c-1-3 1-7 3-7z"/><path d="M28 8a14 14 0 0 1 12 12M27 14a8 8 0 0 1 7 7"/></symbol>
    <symbol id="i-games" viewBox="0 0 48 48"><path d="M14 16h20c6 0 9 6 9 14s-2 10-5 10-5-5-8-5H18c-3 0-5 5-8 5s-5-2-5-10 3-14 9-14z"/><path d="M15 23v8M11 27h8M24 16c0-4 2-6 6-6"/><circle cx="32" cy="25" r="1.5"/><circle cx="36" cy="29" r="1.5"/></symbol>
    <symbol id="i-care" viewBox="0 0 48 48"><path d="M24 42L8 27C2 21 4 10 13 9c5 0 8 3 11 7 3-4 6-7 11-7 9 1 11 12 5 18z"/><path d="M16 22l6 6M14 27l6 6M19 31l5 5M24 16l-6 6 3 3 7-5 6 6"/></symbol>
    <symbol id="i-movies" viewBox="0 0 48 48"><circle cx="22" cy="22" r="17"/><circle cx="22" cy="22" r="3"/><circle cx="22" cy="12" r="4"/><circle cx="22" cy="32" r="4"/><circle cx="12" cy="22" r="4"/><circle cx="32" cy="22" r="4"/><path d="M34 34c3 4 7 6 11 6"/></symbol>
  </defs>
</svg>

<!-- Home screen -->
<section class="screen screen--home">
  <div class="deco deco--right"></div>
  <div class="deco deco--bottom"></div>
  <header class="topbar">
    <div class="brand"><span class="brand-dot"></span>Quorvix</div>
    <div class="search"><span class="search-text">SEARCH</span>
      <span class="search-btn"><svg width="20" height="20" viewBox="0 0 20 20" fill="none" stroke="#fff" stroke-width="2.4"><circle cx="8.5" cy="8.5" r="5.5"/><path d="M13 13l4 4"/></svg></span></div>
  </header>
  <div class="tile" style="left:155px;top:152px"><div class="tile-icon"><svg><use href="#i-rocket"/></svg></div><div class="tile-label">START</div></div>
  <div class="tile" style="left:396px;top:152px"><div class="tile-icon"><svg><use href="#i-tv"/></svg></div><div class="tile-label">TV</div></div>
  <div class="tile" style="left:631px;top:152px"><div class="tile-icon"><svg><use href="#i-radio"/></svg></div><div class="tile-label">RADIO</div></div>
  <div class="tile" style="left:151px;top:388px"><div class="tile-icon"><svg><use href="#i-apps-web"/></svg></div><div class="tile-label">APPS</div></div>
  <div class="tile" style="left:395px;top:388px"><div class="tile-icon"><svg><use href="#i-language"/></svg></div><div class="tile-label">LANGUAGE</div></div>
  <div class="tile" style="left:631px;top:388px"><div class="tile-icon"><svg><use href="#i-clock"/></svg></div><div class="tile-label">CLOCK</div></div>
  <div class="ward-clock"><span class="ward">DEMO WARD</span><span class="time">15:35</span><span class="bed">DEFAULT BED</span></div>
</section>

<!-- Services screen -->
<section class="screen screen--services">
  <div class="deco deco--right"></div>
  <div class="deco deco--bottom"></div>
  <header class="topbar">
    <div class="brand"><span class="brand-dot"></span>Quorvix</div>
    <div class="search" style="left:659px"><span class="search-text">SEARCH</span>
      <span class="search-btn"><svg width="20" height="20" viewBox="0 0 20 20" fill="none" stroke="#fff" stroke-width="2.4"><circle cx="8.5" cy="8.5" r="5.5"/><path d="M13 13l4 4"/></svg></span></div>
  </header>
  <div class="tile" style="left:42px;top:98px"><div class="tile-icon"><svg><use href="#i-video"/></svg></div><div class="tile-label">VIDEO CALLS</div></div>
  <div class="tile" style="left:211px;top:98px"><div class="tile-icon"><div class="icon-placeholder" role="img" aria-label="Meditating figure icon"></div></div><div class="tile-label">RELAX</div></div>
  <div class="tile" style="left:374px;top:98px"><div class="tile-icon"><svg><use href="#i-globe"/></svg></div><div class="tile-label">INTERNET</div></div>
  <div class="tile" style="left:539px;top:98px"><div class="tile-icon"><svg><use href="#i-clinical"/></svg></div><div class="tile-label">CLINICAL</div></div>
  <div class="tile" style="left:705px;top:98px"><div class="tile-icon"><svg><use href="#i-education"/></svg></div><div class="tile-label">EDUCATION</div></div>
  <div class="tile" style="left:870px;top:98px"><div class="tile-icon"><svg><use href="#i-meal"/></svg></div><div class="tile-label">MEAL</div></div>

  <div class="tile" style="left:38px;top:281px"><div class="tile-icon"><svg><use href="#i-books"/></svg></div><div class="tile-label">BOOKS</div></div>
  <div class="tile" style="left:208px;top:281px"><div class="tile-icon"><svg><use href="#i-gear"/></svg></div><div class="tile-label">SETTINGS</div></div>
  <div class="tile" style="left:373px;top:281px"><div class="tile-icon"><svg><use href="#i-phone-apps"/></svg></div><div class="tile-label">APPS</div></div>
  <div class="tile" style="left:538px;top:281px"><div class="tile-icon"><div class="icon-placeholder" role="img" aria-label="Concierge staff icon"></div></div><div class="tile-label">CONCIERGE</div></div>
  <div class="tile" style="left:704px;top:281px"><div class="tile-icon"><svg><use href="#i-phone"/></svg></div><div class="tile-label">PHONE</div></div>
  <div class="tile" style="left:869px;top:281px"><div class="tile-icon"></div><div class="tile-label">BARCODE</div></div>

  <div class="tile" style="left:40px;top:465px"><div class="tile-icon"><svg><use href="#i-games"/></svg></div><div class="tile-label">GAMES</div></div>
  <div class="tile" style="left:206px;top:465px"><div class="tile-icon"><svg><use href="#i-care"/></svg></div><div class="tile-label">MY CARE</div></div>
  <div class="tile" style="left:372px;top:465px"><div class="tile-icon"><svg><use href="#i-movies"/></svg></div><div class="tile-label">MOVIES</div></div>
  <div class="ward-clock"><span class="ward">DEMO WARD</span><span class="time">15:35</span><span class="bed">DEFAULT BED</span></div>
</section>

<!-- Language screen -->
<section class="screen screen--languages">
  <div class="deco deco--right"></div>
  <div class="deco deco--bottom"></div>
  <header class="topbar">
    <div class="brand"><span class="brand-dot"></span>Quorvix</div>
    <div class="search" style="left:664px"><span class="search-text">SEARCH</span>
      <span class="search-btn"><svg width="20" height="20" viewBox="0 0 20 20" fill="none" stroke="#fff" stroke-width="2.4"><circle cx="8.5" cy="8.5" r="5.5"/><path d="M13 13l4 4"/></svg></span></div>
  </header>

  <div class="tile" style="left:44px;top:151px"><div class="tile-icon">
    <svg class="flag" viewBox="0 0 60 30"><rect width="60" height="30" fill="#2b3f8f"/><path d="M0 0l60 30M60 0L0 30" stroke="#fff" stroke-width="6"/><path d="M0 0l60 30M60 0L0 30" stroke="#d6232f" stroke-width="2"/><path d="M30 0v30M0 15h60" stroke="#fff" stroke-width="10"/><path d="M30 0v30M0 15h60" stroke="#d6232f" stroke-width="6"/></svg>
  </div><div class="tile-label">ENGLISH</div></div>
  <div class="tile" style="left:232px;top:151px"><div class="tile-icon">
    <svg class="flag" viewBox="0 0 3 2"><rect width="1" height="2" fill="#3f4a9a"/><rect x="1" width="1" height="2" fill="#fff"/><rect x="2" width="1" height="2" fill="#f24b55"/></svg>
  </div><div class="tile-label">FRENCH</div></div>
  <div class="tile" style="left:414px;top:151px"><div class="tile-icon">
    <svg class="flag" viewBox="0 0 3 2"><rect width="3" height="2" fill="#e6e6e6"/><circle cx="1.5" cy="1" r=".45" fill="#e60012"/></svg>
  </div><div class="tile-label">JAPANESE</div></div>
  <div class="tile" style="left:593px;top:151px"><div class="tile-icon">
    <svg class="flag" viewBox="0 0 3 2"><rect width="1" height="2" fill="#1ea55a"/><rect x="1" width="1" height="2" fill="#fff"/><rect x="2" width="1" height="2" fill="#c0392b"/></svg>
  </div><div class="tile-label">ITALIAN</div></div>
  <div class="tile" style="left:772px;top:151px"><div class="tile-icon">
    <svg class="flag" viewBox="0 0 3 2"><rect width="3" height="2" fill="#e8222a"/><rect y=".5" width="3" height="1" fill="#f4c21d"/></svg>
  </div><div class="tile-label">SPANISH</div></div>

  <div class="tile" style="left:44px;top:338px"><div class="tile-icon">
    <svg class="flag" viewBox="0 0 30 30" style="width:64px;height:64px"><rect width="30" height="30" fill="#e5432f"/><path d="M7 4l1.2 3.6H12l-3 2.2 1.2 3.6L7 11.2 3.8 13.4 5 9.8 2 7.6h3.8z" fill="#f9d21b"/><circle cx="13" cy="4" r=".8" fill="#f9d21b"/><circle cx="15" cy="7" r=".8" fill="#f9d21b"/><circle cx="15" cy="10" r=".8" fill="#f9d21b"/><circle cx="13" cy="13" r=".8" fill="#f9d21b"/></svg>
  </div><div class="tile-label">CHINESE</div></div>
  <div class="tile" style="left:232px;top:338px"><div class="tile-icon">
    <svg class="flag" viewBox="0 0 30 20"><rect width="30" height="20" fill="#e5161e"/><path d="M15 4l1.8 5.3h5.6l-4.5 3.3 1.7 5.3L15 14.6l-4.6 3.3 1.7-5.3-4.5-3.3h5.6z" fill="#ffde00"/></svg>
  </div><div class="tile-label">VIETNAMESE</div></div>
  <div class="tile" style="left:414px;top:338px"><div class="tile-icon">
    <svg class="flag" viewBox="0 0 3 2" style="width:86px"><rect width="3" height=".67" fill="#111"/><rect y=".67" width="3" height=".67" fill="#dd0025"/><rect y="1.33" width="3" height=".67" fill="#ffd84a"/></svg>
  </div><div class="tile-label">GERMAN</div></div>
  <div class="tile" style="left:593px;top:338px"><div class="tile-icon">
    <svg class="flag" viewBox="0 0 3 2" style="width:84px"><rect width="3" height=".67" fill="#f7a93a"/><rect y=".67" width="3" height=".67" fill="#fff"/><rect y="1.33" width="3" height=".67" fill="#79b52d"/><circle cx="1.5" cy="1" r=".22" fill="none" stroke="#2d3a8c" stroke-width=".05"/></svg>
  </div><div class="tile-label">HINDI</div></div>
  <div class="tile" style="left:772px;top:338px"><div class="tile-icon">
    <svg class="flag" viewBox="0 0 3 2" style="width:82px"><rect x=".75" width="2.25" height=".67" fill="#119d3a"/><rect x=".75" y=".67" width="2.25" height=".67" fill="#fff"/><rect x=".75" y="1.33" width="2.25" height=".67" fill="#000"/><rect width=".75" height="2" fill="#ff0000"/></svg>
  </div><div class="tile-label">ARABIC</div></div>
  <div class="ward-clock"><span class="ward">DEMO WARD</span><span class="time">15:35</span><span class="bed">DEFAULT BED</span></div>
</section>

</body>
</html>
```